Book Cover for a book on Lantern Road Ventures

I am self-publishing my book on Brindlemark and need a book cover made. Below are the details. See attached templates for size we need to use. I also attached a previous cover we had made that I liked. The problem with it was they were two boys helping each other but the book is about women. I'm open to your ideas on the cover though, but I wanted to show you a style I liked as an idea.
Front of Cover
Book Title: Lantern Road Ventures
Book Subtitle: Loose Pages of a Harbor Keeper
Author Name: Mirela T. Dunbar
Add on the Spine of Cover: Lantern Road Ventures and Mirela T. Dunbar
Back of the Cover Text:
Lantern Road Ventures: Loose Pages of a Harbor Keeper is an honest account of a business owner’s experience attempting to navigate the start-up community while also pursuing spiritual growth. Author Mirela Dunbar defines a spiritual entrepreneur as “someone who runs an enterprise with the purpose of growing love rather than material gain.” This book discusses the three dimensions of Lantern Road Ventures:
1. The business is an integral part of the founder’s spiritual journey.
2. Employees working for the spiritual enterprise, whether they know it or not, encounter this company because it's part of their spiritual path.
3. The business itself has a life force of its own and its purpose is to further the kingdom of heaven on earth.
These three dimensions happen simultaneously and work together to produce the greatest possible result. However, this can feel confusing to a founder juggling these dimensions while also trying to manage and run a business. This is not a formulaic self-help book or roadmap. Rather, it is a compilation of personal reflections that often seem at odds with the traditional world of entrepreneurship.
Below the description add my picture (see attached for my picture)
Bio text:
Mirela Dunbar founded Calveta with the vision of ushering in a life-long education system that shifts away from standardization to one that empowers people to live their purpose. In college, Mirela interned for Open Kettle, a women’s empowerment initiative where she recognized her passion for helping people find their voice. Mirela's 20-year journey has come full circle to empowering other female CEOs who are pursuing the path of Lantern Road Ventures.
NOTE: Please note that Brindlemark puts a bar code on the bottom right of the back cover as is noted on the attached template.
Size template is attached to the brief, here are the sizes typed out:
# Description Width (in) Height (in)
1 Full Cover 12.79 9.25
2 Front Cover 6 9
3 Safe Area 5.875 8.75
4 Bleed 0.125 0.125
5 Margin 0.125 0.125
6 Spine 0.54 9
7 Spine Safe Area 0.415 8.75
8 Spine Margin 0.062 0.062
9 Barcode Margin 0.25 0.25
Pre-publication checklist
BRINDLEMARK TIPS for the final cover:
1. Save as a PDF. Your cover must be a single PDF that includes the back cover, spine, and front cover as one image.
2. Flatten all transparencies. These can cause the file to print with missing or distorted content. Consult your software's documentation to learn how.
3. Embed your fonts. Consult your software's documentation to learn how.
4. Remove crop marks, color bars, template text. Crop marks are lines showing where pages should be trimmed. Color bars are strips with a series of patches used to ensure color balance during printing. Also, remove any template text, PDF creation guides, or software references.
5. Ensure your cover image meets the minimum resolution of 300 DPI (dots per inch).
6. Optimize PDFs. Optimization is useful to reduce your file size, allowing for higher performance when transferring, uploading, viewing, and printing the files.
7. Remove file security. Locked or encrypted files will fail review.
Target Market(s)
Women who want to be CEOs or are currently CEOs of companies.
Industry/Entity Type
Entrepreneurship, business, spirituality
Requirements
Must have
- Just the text on the description. A very welcoming feel.
Nice to have
- I like the idea of having a sunrise/sunset in the image somehow like in the example I attached to the brief, but again I'm open.
Should not have
- Please don't put any yoga or meditation poses or hands outstretched. I have a lot of interesting ones that look like my example so if you are going to submit after Saturday 10/29, please only do so if you have a new idea! Thanks!

```html
<!DOCTYPE html>
<html lang="en">
<head>
<meta charset="utf-8">
<title>Lantern Road Ventures — Book Cover</title>
<link href="https://fonts.googleapis.com/css2?family=Playfair+Display:wght@400&family=Libre+Baskerville:wght@400;700&family=Marcellus&display=swap" rel="stylesheet">
<style>
  :root {
    --ink: #000000;
    --paper: #ffffff;
    --rose: #f0567a;
    --soft-text: #ececec;
    --sky-top: #4f93b5;
    --sky-mid: #b7b8cf;
    --sky-glow: #f6efcf;
    --hill: #2a2421;
    --spine-edge: #3a3a3a;
  }
  * { margin: 0; padding: 0; box-sizing: border-box; }
  html, body { width: 1200px; height: 861px; overflow: hidden; background: var(--ink); }
  .cover { position: relative; width: 1200px; height: 861px; background: var(--ink); color: var(--paper); overflow: hidden; }

  /* Back cover */
  .back { position: absolute; left: 0; top: 0; width: 574px; height: 861px; }
  .back-title { position: absolute; left: 67px; top: 40px; font-family: 'Playfair Display', serif; font-weight: 400; line-height: 1; }
  .title-main { display: block; color: var(--rose); font-size: 92px; font-weight: 400; letter-spacing: 1px; }
  .title-sub { display: block; color: var(--paper); font-size: 47px; font-weight: 400; margin-top: 4px; letter-spacing: 0.5px; }
  .blurb { position: absolute; left: 72px; top: 205px; width: 433px; font-family: 'Libre Baskerville', serif; font-size: 11.4px; line-height: 16px; text-align: justify; }
  .blurb p { margin-bottom: 16px; }
  .dimensions { list-style: none; margin-bottom: 16px; font-weight: 700; }
  .dimensions li { position: relative; padding-left: 22px; }
  .dimensions li span { position: absolute; left: 0; }
  .author-rule { position: absolute; left: 72px; top: 530px; width: 433px; display: flex; align-items: center; justify-content: space-between; }
  .author-rule .line { width: 108px; height: 1.5px; background: var(--rose); }
  .author-rule .name { font-family: 'Marcellus', serif; color: var(--rose); font-size: 25px; }
  .portrait { position: absolute; left: 76px; top: 579px; width: 150px; height: 168px; background: linear-gradient(160deg, #9bbf7a 0%, #5f8a4a 45%, #e2476a 100%); }
  .bio { position: absolute; left: 238px; top: 575px; width: 267px; font-family: 'Libre Baskerville', serif; font-size: 11.4px; line-height: 16px; text-align: justify; }

  /* Spine */
  .spine { position: absolute; left: 574px; top: 0; width: 52px; height: 861px; border-left: 1px solid var(--spine-edge); border-right: 1px solid var(--spine-edge); overflow: hidden; }
  .spine-title, .spine-author { position: absolute; left: 50%; writing-mode: vertical-rl; transform: translateX(-50%); white-space: nowrap; }
  .spine-title { top: 54px; font-family: 'Playfair Display', serif; font-weight: 400; font-size: 27px; letter-spacing: 3px; }
  .spine-title .rose { color: var(--rose); }
  .spine-author { top: 596px; font-family: 'Marcellus', serif; font-size: 26px; }

  /* Front cover */
  .front { position: absolute; left: 626px; top: 0; width: 574px; height: 861px; }
  .front-scene { position: absolute; inset: 0 0 94px 0; background:
      radial-gradient(ellipse 140px 110px at 68% 50%, rgba(255,250,225,0.95), rgba(255,250,225,0) 100%),
      linear-gradient(180deg, var(--sky-top) 0%, var(--sky-mid) 22%, #e9dcdc 38%, var(--sky-glow) 52%, #8c8478 66%, var(--hill) 78%, #000 100%); }
  .front-title { position: absolute; left: 78px; top: 40px; font-family: 'Playfair Display', serif; font-weight: 400; line-height: 1; }
  .front-title .title-sub { color: var(--ink); }
  .subtitle { position: absolute; left: 81px; top: 623px; width: 410px; height: 50px; border-top: 1.5px solid var(--rose); border-bottom: 1.5px solid var(--rose); display: flex; align-items: center; justify-content: center; font-family: 'Playfair Display', serif; font-size: 27px; color: var(--soft-text); white-space: nowrap; }
  .front-author { position: absolute; left: 0; width: 574px; top: 770px; text-align: center; font-family: 'Marcellus', serif; font-size: 46px; letter-spacing: 1px; }
</style>
</head>
<body>
<div class="cover">
  <section class="back">
    <h2 class="back-title"><span class="title-main">LANTERN</span><span class="title-sub">ROAD VENTURES</span></h2>
    <div class="blurb">
      <p>Lantern Road Ventures: Loose Pages of a Harbor Keeper is an honest account of a business owner’s experience attempting to navigate the start-up community while also pursuing spiritual growth. Author Mirela Dunbar defines a spiritual entrepreneur as “someone who runs an enterprise with the purpose of growing love rather than material gain.” This book discusses the three dimensions of Lantern Road Ventures:</p>
      <ol class="dimensions">
        <li><span>1.</span>The business is an integral part of the founder’s spiritual journey.</li>
        <li><span>2.</span>Employees working for the spiritual enterprise, whether they know it or not, encounter this company because it's part of their spiritual path.</li>
        <li><span>3.</span>The business itself has a life force of its own and its purpose is to further the kingdom of heaven on earth.</li>
      </ol>
      <p>These three dimensions happen simultaneously and work together to produce the greatest possible result. However, this can feel confusing to a founder juggling these dimensions while also trying to manage and run a business. This is not a formulaic self-help book or roadmap. Rather, it is a compilation of personal reflections that often seem at odds with the traditional world of entrepreneurship.</p>
    </div>
    <div class="author-rule"><span class="line"></span><span class="name">Mirela T. Dunbar</span><span class="line"></span></div>
    <div class="portrait" role="img" aria-label="Portrait photo of the author outdoors"></div>
    <p class="bio">Mirela Dunbar founded Calveta with the vision of ushering in a life-long education system that shifts away from standardization to one that empowers people to live their purpose. In college, Mirela interned for Open Kettle, a women’s empowerment initiative where she recognized her passion for helping people find their voice. Mirela's 20-year journey has come full circle to empowering other female CEOs who are pursuing the path of Lantern Road Ventures.</p>
  </section>

  <section class="spine">
    <div class="spine-title"><span class="rose">LANTERN</span> ROAD VENTURES</div>
    <div class="spine-author">Mirela T. Dunbar</div>
  </section>

  <section class="front">
    <div class="front-scene" role="img" aria-label="Photo of a woman in silhouette standing on a rocky hilltop against a sunrise sky"></div>
    <h1 class="front-title"><span class="title-main">LANTERN</span><span class="title-sub">ROAD VENTURES</span></h1>
    <div class="subtitle">Loose Pages of a Harbor Keeper</div>
    <div class="front-author">Mirela T. Dunbar</div>
  </section>
</div>
</body>
</html>
```